Lumenfield Holdings

Professional looking business card using darker colours
I do not yet have a logo for the company so feel free to suggest
The business is based on consultancy and project management
Based in Melbourne
Business card can omit the word "Holdings" and can be Lumenfield consulting etc.

Business

Contact Name on card : Tom Verisco Contact number : +61412 305 617 Email address will be confirmed shortly.

```html
<!DOCTYPE html>
<html lang="en">
<head>
<meta charset="utf-8">
<title>Lumenfield Consulting – Business Card</title>
<link rel="stylesheet" href="https://fonts.googleapis.com/css2?family=Exo+2:wght@400;500;700&display=swap">
<style>
  :root {
    --page-bg: #e4eaec;
    --card-white: #ffffff;
    --navy: #10127a;
    --navy-deep: #0b0c63;
    --blue-mid: #1d47c2;
    --blue-glow: #2fb0ec;
    --ink: #3b3d4a;
    --shadow: rgba(40, 55, 70, 0.16);
  }
  * { box-sizing: border-box; margin: 0; padding: 0; }
  html, body { width: 1200px; height: 1200px; overflow: hidden; }
  body {
    background: var(--page-bg);
    font-family: "Exo 2", sans-serif;
    color: var(--ink);
    display: flex;
    flex-direction: column;
    align-items: center;
    justify-content: center;
    gap: 56px;
  }
  .card {
    position: relative;
    width: 860px;
    height: 491px;
    background: var(--card-white);
    border-radius: 6px;
    box-shadow: 0 10px 30px var(--shadow);
    overflow: hidden;
  }

  /* ---------- Front ---------- */
  .front__panel {
    position: absolute;
    top: 16px; right: 16px; left: 78px;
    height: 318px;
    border-radius: 14px 14px 14px 0;
    background: radial-gradient(ellipse 55% 60% at 48% 44%, var(--blue-glow) 0%, var(--blue-mid) 42%, var(--navy) 78%, var(--navy-deep) 100%);
  }
  .front__rule {
    position: absolute;
    left: 96px; top: 16px;
    width: 5px; height: 372px;
    background: var(--navy-deep);
  }
  .front__name {
    position: absolute;
    right: 44px; top: 252px;
    font-size: 52px;
    font-weight: 700;
    line-height: 1;
    color: var(--card-white);
    white-space: nowrap;
  }
  .contact {
    position: absolute;
    left: 36px; top: 398px;
    font-size: 19px;
    line-height: 1.35;
    color: var(--ink);
  }
  .contact__row { display: flex; gap: 10px; }
  .contact__label { width: 20px; font-weight: 700; color: var(--navy); }

  /* ---------- Back ---------- */
  .back__copy {
    position: absolute;
    left: 40px; top: 34px;
    width: 440px;
    font-size: 18px;
    line-height: 1.32;
    color: var(--ink);
  }
  .back__brand {
    position: absolute;
    right: 40px; top: 36px;
    width: 300px;
  }
  .back__name {
    font-size: 27px;
    font-weight: 700;
    line-height: 1.1;
    color: var(--navy);
    white-space: nowrap;
  }
  .services {
    list-style: none;
    margin-top: 18px;
    font-size: 18px;
    line-height: 1.3;
    color: var(--ink);
  }
  .services li::before { content: "· "; }
  .back__band {
    position: absolute;
    left: 16px; right: 45px; bottom: 16px;
    height: 128px;
    border-radius: 12px 0 12px 12px;
    background: linear-gradient(100deg, var(--navy) 0%, var(--blue-mid) 55%, var(--navy) 100%);
    display: flex;
    align-items: center;
    padding-left: 46px;
  }
  .back__tagline {
    font-size: 22px;
    font-weight: 500;
    color: var(--card-white);
    letter-spacing: 0.3px;
  }
  .back__rule {
    position: absolute;
    right: 40px; bottom: 16px;
    width: 5px; height: 200px;
    background: var(--navy-deep);
  }
</style>
</head>
<body>

  <section class="card card--front" aria-label="Business card front">
    <div class="front__panel"></div>
    <div class="front__rule"></div>
    <div class="front__name">Lumenfield Consulting</div>
    <div class="contact">
      <div class="contact__row"><span class="contact__label"></span><span>Tom Verisco</span></div>
      <div class="contact__row"><span class="contact__label">M</span><span>+61412 305 617</span></div>
      <div class="contact__row"><span class="contact__label">E</span><span>tom.verisco@lumenfield.com</span></div>
    </div>
  </section>

  <section class="card card--back" aria-label="Business card back">
    <p class="back__copy">Consulting on omnihill oudisquam, omnihic iliquat molorec torendae quodest, eaquis qui que que ex es Odigenia exerum voluptaquo magnaturi quam unt re solum qui corro magnihi tincid que ipsum que Odigenia exerum voluptaquo magnaturi quam unt re solum qui corro magnihi tincid que.</p>
    <div class="back__brand">
      <div class="back__name">Lumenfield Consulting</div>
      <ul class="services">
        <li>Consultancy</li>
        <li>Management</li>
        <li>Training</li>
        <li>Skilled services</li>
        <li>International</li>
      </ul>
    </div>
    <div class="back__rule"></div>
    <div class="back__band">
      <span class="back__tagline">Professional service with over 10 years experience</span>
    </div>
  </section>

</body>
</html>
```